Business Cards Design for the electrical wholesaler: clean bold dynamic :)

We need a business card design that would follow our latest brand guidelines. As an electrical wholesaler we want to bring a fresh look and feel into the industry. The design should be clean bold and dynamic. It should come alive with the renewed energy of our green colour. Our grey colour should keep things balanced and complement the notion of maturity and responsibility. We employ Lato as a corporate font however are not bound by this font and we’re open to interpretation here.

Target Market(s)

Electrical contractors

Industry/Entity Type

Business

Contact Information for Business Card

Logo
Name & Surname: Olena Dovbush
Job Title: Director of Marketing
Email: helen.dovbush@mailvane.example
Cell phone: XXX.XXX.XXXX
Address: 20917 - 87 Ave. Edmonton, AB, Canada. T6K 2R8
Business Phone: 780.555.0187
Website: www.qorvil.example

Font styles to use
Other font styles liked:
• Lato

Requirements
Must have
• Logo & website
Nice to have
• Brand elements - some of them you may find in the attached Brand Guidelines (e.g. three lines on the background signifying "W")

```html
<!DOCTYPE html>
<html lang="en">
<head>
<meta charset="utf-8">
<title>Qorvil business cards</title>
<link href="https://fonts.googleapis.com/css2?family=Lato:wght@400;700;900&display=swap" rel="stylesheet">
<style>
  :root {
    --page: #e6e3df;
    --card: #0b0b0c;
    --card-sheen: #1c1d1f;
    --green: #7cc242;
    --green-light: #9fd66a;
    --white: #ffffff;
    --grey: #c9ccce;
  }
  * { margin: 0; padding: 0; box-sizing: border-box; }
  html, body {
    width: 1200px; height: 1200px; overflow: hidden;
    background: var(--page);
    font-family: "Lato", Arial, sans-serif;
  }
  .sheet { position: relative; width: 1200px; height: 1200px; }
  .card {
    position: absolute; left: 180px; width: 840px; height: 480px;
    border-radius: 6px; overflow: hidden;
    background: linear-gradient(120deg, var(--card) 0%, var(--card) 45%, var(--card-sheen) 70%, var(--card) 100%);
    box-shadow: 0 14px 30px rgba(0,0,0,.25);
    color: var(--white);
  }
  .card--front { top: 80px; }
  .card--back { top: 640px; }

  .brand { display: flex; align-items: center; gap: 22px; }
  .brand__square { width: 70px; height: 70px; background: var(--green); }
  .brand__name { font-weight: 900; color: var(--white); line-height: 1; }

  .card--front .brand {
    position: absolute; left: 50%; top: 50%; transform: translate(-50%, -50%);
  }
  .card--front .brand__name { font-size: 120px; letter-spacing: -2px; }

  .card--back .brand { position: absolute; left: 60px; top: 200px; gap: 14px; }
  .card--back .brand__square { width: 40px; height: 40px; }
  .card--back .brand__name { font-size: 64px; letter-spacing: -1px; }

  .divider {
    position: absolute; left: 380px; top: 80px; width: 2px; height: 230px;
    background: var(--green);
  }
  .person { position: absolute; left: 410px; top: 78px; right: 30px; }
  .person__name { font-size: 36px; font-weight: 900; letter-spacing: 1px; text-transform: uppercase; }
  .person__title {
    display: inline-block; margin-top: 4px; padding-bottom: 3px;
    font-size: 16px; font-weight: 700; letter-spacing: 1px; text-transform: uppercase;
    border-bottom: 3px solid var(--green);
  }
  .contacts { list-style: none; margin-top: 22px; }
  .contacts__item {
    display: flex; align-items: center; gap: 12px;
    font-size: 17px; line-height: 30px; color: var(--grey);
  }
  .contacts__icon { width: 18px; height: 18px; flex: none; }
  .address {
    position: absolute; left: 60px; bottom: 48px;
    font-size: 19px; letter-spacing: .5px; color: var(--white);
  }
</style>
</head>
<body>
<main class="sheet">

  <section class="card card--front" aria-label="Card front">
    <div class="brand">
      <span class="brand__square"></span>
      <span class="brand__name">qorvil</span>
    </div>
  </section>

  <section class="card card--back" aria-label="Card back">
    <div class="brand">
      <span class="brand__square"></span>
      <span class="brand__name">qorvil</span>
    </div>

    <span class="divider"></span>

    <div class="person">
      <h1 class="person__name">Olena Dovbush</h1>
      <p class="person__title">Director of Marketing</p>
      <ul class="contacts">
        <li class="contacts__item">
          <svg class="contacts__icon" viewBox="0 0 18 18" fill="none" stroke="#7cc242" stroke-width="1.8"><rect x="5" y="1.5" width="8" height="15" rx="1.5"/><line x1="8" y1="13.5" x2="10" y2="13.5"/></svg>
          +1 780 555 0142
        </li>
        <li class="contacts__item">
          <svg class="contacts__icon" viewBox="0 0 18 18" fill="#7cc242"><path d="M4 1.5l3 3.5-1.6 2a9 9 0 0 0 5.6 5.6l2-1.6 3.5 3-1.8 2.5C8 16 2 10 1.5 3.3z"/></svg>
          780.555.0187
        </li>
        <li class="contacts__item">
          <svg class="contacts__icon" viewBox="0 0 18 18" fill="none" stroke="#7cc242" stroke-width="1.5"><circle cx="9" cy="9" r="7.5"/><ellipse cx="9" cy="9" rx="3.2" ry="7.5"/><line x1="1.5" y1="9" x2="16.5" y2="9"/></svg>
          www.qorvil.example
        </li>
        <li class="contacts__item">
          <svg class="contacts__icon" viewBox="0 0 18 18" fill="#7cc242"><path d="M1 4h16v10H1z"/><path d="M1 4l8 6 8-6" fill="none" stroke="#0b0b0c" stroke-width="1.4"/></svg>
          helen.dovbush@mailvane.example
        </li>
      </ul>
    </div>

    <p class="address">20917 - 87 Ave. Edmonton, AB, Canada. T6K 2R8</p>
  </section>

</main>
</body>
</html>
```